I need a very simple poster with the following quote:
"Cada escolha, uma renĂșncia, isso Ă© a vida"
Which means that to every choice there is a waiver, that's life.

It will be framed and used in my living room.

The poster has to be black and white. It is not mandatory to use commas and quotes.

The design has to be modern, like the references I posted on this board: http://pinboardly.example/marvetu/ideas/

```html
<!DOCTYPE html>
<html lang="pt">
<head>
<meta charset="utf-8">
<title>Cada escolha, uma renúncia</title>
<link href="https://fonts.googleapis.com/css2?family=Oranienbaum&display=swap" rel="stylesheet">
<style>
  :root {
    --poster-bg: #000000;
    --quote-ink: #6f6f6f;
  }
  html, body {
    margin: 0;
    padding: 0;
    width: 854px;
    height: 1200px;
    overflow: hidden;
    background: var(--poster-bg);
  }
  .poster {
    display: block;
    width: 854px;
    height: 1200px;
    background: var(--poster-bg);
  }
  .quote {
    font-family: "Oranienbaum", "Bodoni Moda", serif;
    font-weight: 400;
    font-size: 205px;
    fill: var(--quote-ink);
  }
</style>
</head>
<body>
  <svg class="poster" width="854" height="1200" viewBox="0 0 854 1200" role="img" aria-label="Cada escolha, uma renúncia, isso é a vida">
    <rect width="854" height="1200" fill="var(--poster-bg)"/>
    <g class="quote" text-anchor="middle">
      <text class="quote__line" x="428" y="424" textLength="725" lengthAdjust="spacingAndGlyphs">"Cada escolha,</text>
      <text class="quote__line" x="428" y="616" textLength="720" lengthAdjust="spacingAndGlyphs">uma renúncia,</text>
      <text class="quote__line" x="419" y="807" textLength="619" lengthAdjust="spacingAndGlyphs">isso é a vida"</text>
    </g>
  </svg>
</body>
</html>
```